Business card and stationary for a garage
Motorwerkplaats Holvoort
@ph - changes done .Please check and confirm.- Thanks
@brightpeak
Can you please make another version with #136 as the front and #135 as the back side.
Note 1: Please omit the word "Services" and make the logo a little bit bigger at the back side
Note 2: It's Brembeekhof
Note 3: #135 the back side. The text "Motorwerkplaats Holvoort" is too gray. Just use the original logo and colors.
#ALL
Please use "T" for phonenumber and "F" for fax. Do not use the English abbreviations. Or better use icons.
Nice designs, thank you.
We dont prefer a style like #124-#129 for the back of the card. Its to simple. The service listing can be more attractive like in #121 or #118 (horizontal).
#ALL please do not use english words in business card like "Our services". Use only "Services" as this is also a common word in Dutch.
"Voor alle merken" means "For all brands"

```html
<!DOCTYPE html>
<html lang="nl">
<head>
<meta charset="utf-8">
<title>Motorwerkplaats Holvoort – visitekaartjes</title>
<link rel="stylesheet" href="https://fonts.googleapis.com/css2?family=Arimo:wght@400;700&family=Open+Sans:wght@600;700&display=swap">
<style>
  :root {
    --stage: #1c1c1c;
    --card: #ffffff;
    --red: #e3232a;
    --red-dark: #8c1a20;
    --ink: #3b3b3b;
    --name-red: #c8202a;
    --text: #2e2e2e;
    --rule: #c9c9c9;
    --band-dark: #1e1e1e;
    --band-light: #6a6a6a;
  }
  * { margin: 0; padding: 0; box-sizing: border-box; }
  html, body { width: 1200px; height: 782px; overflow: hidden; }
  body { background: var(--stage); position: relative; font-family: "Arimo", Arial, sans-serif; }

  .card {
    position: absolute; width: 528px; height: 300px;
    background: var(--card); border-radius: 24px; overflow: hidden;
  }
  .card--front-icons { left: 60px; top: 55px; }
  .card--front-letters { left: 627px; top: 55px; }
  .card--back { left: 250px; top: 418px; }

  .wave { position: absolute; left: 0; top: 0; width: 528px; height: 300px; }

  .brand {
    position: absolute; display: flex; align-items: center; gap: 10px;
    color: var(--ink); font-weight: 700; text-transform: uppercase; letter-spacing: 0.5px;
  }
  .brand__mark { width: 16px; height: 16px; background: var(--red); flex: none; }
  .brand__name { line-height: 1.1; }
  .card--front-icons .brand, .card--front-letters .brand { left: 30px; top: 103px; font-size: 19px; }
  .card--back .brand { left: 0; right: 0; top: 72px; justify-content: center; font-size: 28px; }
  .card--back .brand__mark { width: 22px; height: 22px; }

  .divider { position: absolute; left: 296px; top: 48px; width: 1px; height: 130px; background: var(--rule); }

  .contact { position: absolute; left: 315px; top: 55px; }
  .contact__name { color: var(--name-red); font-weight: 700; font-size: 17px; margin-bottom: 15px; }
  .contact__list { list-style: none; font-size: 14px; color: var(--text); }
  .contact__list li { display: flex; align-items: center; height: 21px; }
  .contact__icon { width: 10px; height: 10px; margin-right: 6px; fill: var(--text); flex: none; }
  .contact__letter { width: 10px; margin-right: 6px; font-size: 13px; }

  .address { position: absolute; left: 50px; top: 250px; color: #fff; font-size: 14px; line-height: 19px; }

  .services {
    position: absolute; left: 0; top: 189px; width: 528px; height: 33px;
    background: linear-gradient(90deg, var(--band-light), var(--band-dark) 45%, var(--band-dark));
    color: #fff; font-family: "Open Sans", Arial, sans-serif; font-weight: 700; font-size: 16.5px;
    display: flex; align-items: center; justify-content: center;
    border-bottom: 2px solid #fff;
  }
  .back-foot {
    position: absolute; left: 0; top: 224px; width: 528px; height: 76px;
    background: linear-gradient(90deg, var(--red-dark), var(--red) 60%, var(--red-dark));
    color: #fff; font-size: 14px; text-align: center; padding-top: 27px;
  }
</style>
</head>
<body>
<svg width="0" height="0" style="position:absolute" aria-hidden="true">
  <defs>
    <linearGradient id="redFill" x1="0" x2="1">
      <stop offset="0" stop-color="#8c1a20"/><stop offset="0.6" stop-color="#e3232a"/><stop offset="1" stop-color="#8c1a20"/>
    </linearGradient>
    <linearGradient id="swoosh" x1="0" x2="1">
      <stop offset="0" stop-color="#111"/><stop offset="0.5" stop-color="#444"/><stop offset="0.8" stop-color="#bbb"/><stop offset="1" stop-color="#111"/>
    </linearGradient>
    <symbol id="wave-shape" viewBox="0 0 528 300">
      <path d="M0,230 C140,198 240,262 340,275 C430,287 495,256 528,226 L528,300 L0,300 Z" fill="url(#swoosh)"/>
      <path d="M0,241 C140,210 240,270 340,281 C430,290 495,264 528,238 L528,300 L0,300 Z" fill="#fff"/>
      <path d="M0,246 C140,216 240,276 340,285 C430,293 495,270 528,244 L528,300 L0,300 Z" fill="url(#redFill)"/>
    </symbol>
    <symbol id="i-phone" viewBox="0 0 10 10"><path d="M2 0.5 L3.8 2.6 L2.9 3.6 Q4.2 6 6.4 7.1 L7.4 6.2 L9.5 8 L8.2 9.5 Q2.5 8.5 0.5 1.8 Z"/></symbol>
    <symbol id="i-fax" viewBox="0 0 10 10"><rect x="2.5" y="0.5" width="5" height="3"/><rect x="0.5" y="4" width="9" height="4.5" rx="1"/><rect x="2.5" y="7" width="5" height="2.5" fill="#fff"/></symbol>
    <symbol id="i-mail" viewBox="0 0 10 10"><rect x="0.5" y="2" width="9" height="6.5" rx="1"/><path d="M1 2.5 L5 6 L9 2.5" stroke="#fff" fill="none" stroke-width="1"/></symbol>
    <symbol id="i-web" viewBox="0 0 10 10"><circle cx="5" cy="5" r="4.5"/><path d="M0.5 5 H9.5 M5 0.5 Q2.5 5 5 9.5 M5 0.5 Q7.5 5 5 9.5" stroke="#fff" fill="none" stroke-width="0.8"/></symbol>
  </defs>
</svg>

<section class="card card--front-icons">
  <svg class="wave" aria-hidden="true"><use href="#wave-shape"/></svg>
  <div class="brand"><span class="brand__mark"></span><span class="brand__name">Motorwerkplaats<br>Holvoort</span></div>
  <div class="divider"></div>
  <div class="contact">
    <p class="contact__name">Ruben Kalverda</p>
    <ul class="contact__list">
      <li><svg class="contact__icon"><use href="#i-phone"/></svg>030-4417825</li>
      <li><svg class="contact__icon"><use href="#i-fax"/></svg>030-4417836</li>
      <li><svg class="contact__icon"><use href="#i-mail"/></svg>info@mwholvoort.nl</li>
      <li><svg class="contact__icon"><use href="#i-web"/></svg>www.mwholvoort.nl</li>
    </ul>
  </div>
  <p class="address">Brembeekhof 20<br>3712 KP Holvoort</p>
</section>

<section class="card card--front-letters">
  <svg class="wave" aria-hidden="true"><use href="#wave-shape"/></svg>
  <div class="brand"><span class="brand__mark"></span><span class="brand__name">Motorwerkplaats<br>Holvoort</span></div>
  <div class="divider"></div>
  <div class="contact">
    <p class="contact__name">Ruben Kalverda</p>
    <ul class="contact__list">
      <li><span class="contact__letter">T</span>030-4417825</li>
      <li><span class="contact__letter">F</span>030-4417836</li>
      <li><svg class="contact__icon"><use href="#i-mail"/></svg>info@mwholvoort.nl</li>
      <li><svg class="contact__icon"><use href="#i-web"/></svg>www.mwholvoort.nl</li>
    </ul>
  </div>
  <p class="address">Brembeekhof 20<br>3712 KP Holvoort</p>
</section>

<section class="card card--back">
  <div class="brand"><span class="brand__mark"></span><span class="brand__name">Motorwerkplaats Holvoort</span></div>
  <div class="services">Onderhoud&nbsp; | APK | Banden | Airco | Voor alle merken</div>
  <div class="back-foot">Brembeekhof 20, 3712 KP Holvoort</div>
</section>
</body>
</html>
```